Business Card Design for Funky New Cloud Security Start-up

We're looking for kick ass business cards to make use stand out from the crowd in a world that's dominated by dull, boring, blue logos.

We have a logo (designed here on pixel forum) and we'd like to build on the brand theme of "Security made simple."

Please use following details for sample:

Martin Colby
CEO
+61 (0)4077 518 206
mart@quenvo.com

2714/58 Harwood Street
Sydney NSW 2000
Australia

Target Market(s)

Customers will be large enterprise clients - typically VP level. Also resellers of our product who are mid-tier.

Industry/Entity Type

Business

Font styles to use
Sans Serif

Requirements
Must have
• Use the colour scheme from the attached logo
Do not put space for a fax - it's old school
Easy to use on nova press
Use a font that complements the logo font

```html
<!DOCTYPE html>
<html lang="en">
<head>
<meta charset="utf-8">
<title>Quenvo business card</title>
<link rel="stylesheet" href="https://fonts.googleapis.com/css2?family=Quicksand:wght@500;600&display=swap">
<style>
  :root {
    --page-bg: #eceeee;
    --silver-edge: #d9d9d9;
    --silver-light: #fbfbfb;
    --silver-mid: #e6e6e6;
    --blue-light: #2aa3d8;
    --blue-mid: #0e5ea6;
    --blue-deep: #213f86;
    --ink: #2b2b2b;
    --white: #ffffff;
  }
  * { box-sizing: border-box; margin: 0; padding: 0; }
  html, body { width: 1130px; height: 1200px; overflow: hidden; }
  body {
    background: var(--page-bg);
    font-family: "Quicksand", sans-serif;
    position: relative;
  }
  .card {
    position: absolute;
    width: 859px;
    height: 497px;
    background: linear-gradient(90deg, var(--silver-edge) 0%, var(--silver-mid) 18%, var(--silver-light) 48%, var(--silver-light) 58%, var(--silver-mid) 82%, var(--silver-edge) 100%);
    box-shadow: 8px 10px 14px rgba(0,0,0,0.28);
    overflow: hidden;
  }
  .card--front { left: 136px; top: 79px; }
  .card--back { left: 138px; top: 629px; }
  .card__band { position: absolute; left: 0; top: 0; width: 859px; height: 497px; }

  .brand {
    position: absolute;
    left: 0; right: 0; top: 112px;
    text-align: center;
    font-weight: 500; font-size: 120px; line-height: 1;
    color: var(--ink);
  }
  .tagline {
    position: absolute; left: 0; right: 0; top: 385px;
    text-align: center; color: var(--white);
    font-weight: 600; font-size: 45px; line-height: 1;
  }

  .person { position: absolute; left: 0; right: 0; text-align: center; color: var(--white); font-weight: 500; line-height: 1; }
  .person__name { top: 46px; font-size: 47px; }
  .person__role { top: 106px; font-size: 45px; }

  .contact { position: absolute; left: 240px; top: 220px; color: var(--ink); font-weight: 500; font-size: 30px; line-height: 38px; }
  .contact__row { display: flex; align-items: center; }
  .contact__icon { width: 24px; height: 24px; margin-right: 8px; flex: none; }
  .contact__gap { height: 37px; }
  .contact__indent { padding-left: 32px; }
</style>
</head>
<body>
  <section class="card card--front">
    <svg class="card__band" viewBox="0 0 859 497" aria-hidden="true">
      <defs>
        <linearGradient id="frontBlue" x1="0" y1="0" x2="0" y2="1">
          <stop offset="0" stop-color="#2aa3d8"/>
          <stop offset="0.45" stop-color="#0e5ea6"/>
          <stop offset="1" stop-color="#213f86"/>
        </linearGradient>
        <linearGradient id="frontSilver" x1="0" y1="0" x2="1" y2="0">
          <stop offset="0" stop-color="#ffffff"/>
          <stop offset="0.5" stop-color="#9a9a9a"/>
          <stop offset="1" stop-color="#ffffff"/>
        </linearGradient>
      </defs>
      <path d="M0 332 Q430 292 859 332 L859 344 Q430 304 0 344 Z" fill="url(#frontSilver)"/>
      <path d="M0 344 Q430 304 859 344 L859 497 L0 497 Z" fill="url(#frontBlue)"/>
    </svg>
    <p class="brand">Quenvo</p>
    <p class="tagline">Security made simple</p>
  </section>

  <section class="card card--back">
    <svg class="card__band" viewBox="0 0 859 497" aria-hidden="true">
      <defs>
        <linearGradient id="backBlue" x1="0" y1="0" x2="0" y2="1">
          <stop offset="0" stop-color="#213f86"/>
          <stop offset="0.55" stop-color="#0e5ea6"/>
          <stop offset="1" stop-color="#2aa3d8"/>
        </linearGradient>
        <linearGradient id="backSilver" x1="0" y1="0" x2="1" y2="0">
          <stop offset="0" stop-color="#ffffff"/>
          <stop offset="0.5" stop-color="#9a9a9a"/>
          <stop offset="1" stop-color="#ffffff"/>
        </linearGradient>
      </defs>
      <path d="M0 140 Q430 188 859 140 L859 152 Q430 200 0 152 Z" fill="url(#backSilver)"/>
      <path d="M0 0 L859 0 L859 140 Q430 188 0 140 Z" fill="url(#backBlue)"/>
    </svg>
    <p class="person person__name">Martin Colby</p>
    <p class="person person__role">CEO</p>

    <div class="contact">
      <div class="contact__row">
        <svg class="contact__icon" viewBox="0 0 24 24" aria-hidden="true"><path d="M6.5 3 L9.5 3 L10.5 8 L8.3 9.6 Q10 14 14.4 15.7 L16 13.5 L21 14.5 L21 17.5 Q20 21 16.5 20.5 Q5 18 3.5 7.5 Q3 4 6.5 3 Z" fill="#2b2b2b"/></svg>
        <span>+61 (0)4077 518 206</span>
      </div>
      <div class="contact__row">
        <svg class="contact__icon" viewBox="0 0 24 24" aria-hidden="true"><rect x="2.5" y="6" width="19" height="13" fill="none" stroke="#2b2b2b" stroke-width="1.8"/><path d="M2.5 6 L12 13.5 L21.5 6 M2.5 19 L9.5 12 M21.5 19 L14.5 12" fill="none" stroke="#2b2b2b" stroke-width="1.6"/></svg>
        <span>mart@quenvo.com</span>
      </div>
      <div class="contact__gap"></div>
      <div class="contact__row">
        <svg class="contact__icon" viewBox="0 0 24 24" aria-hidden="true"><path d="M1.5 10 L12 3 L22.5 10 Z" fill="#2b2b2b"/><rect x="3.5" y="11" width="17" height="10" fill="#2b2b2b"/><rect x="9.5" y="14" width="5" height="7" fill="#ffffff"/></svg>
        <span>2714/58 Harwood Street</span>
      </div>
      <div class="contact__indent">Sydney NSW 2000</div>
      <div class="contact__indent">Australia</div>
    </div>
  </section>
</body>
</html>
```